Pitch deck power point presentation template

I need a power point template for a pitch deck for a startup biotechnology company using the logo we purchased from tallyvane. It should have a cover page and content pages that we can adapt to fit multiple presentations. It should have a page for the team and advisors, and pages for graphs and charts, also pages that have space to add pictures to give background information, and then some with general pages with some blank space. I want it to catch the eye but also be very professional looking.
Updates

The original deadline was only one day from posting for some reason, I extended to 5 days to allow more time.

Target Market(s)

Investors

Industry/Entity Type

Biotechnology

Font styles to use
Serif
Sans Serif

Colors
0054AA
0677BA
7BADD7
CADEEF
E8F1F8

Requirements
Must have
• The logo and the blue color from the logo as the primary color used
Nice to have
• other layouts that we can select from

```html
<!DOCTYPE html>
<html lang="en">
<head>
<meta charset="utf-8">
<title>Halcyra Therapeutics – Pitch Deck Template</title>
<link href="https://fonts.googleapis.com/css2?family=Montserrat:wght@400;500;600;700;800&display=swap" rel="stylesheet">
<style>
:root{
  --blue:#0b95d4;
  --blue-deep:#0a6fb8;
  --teal:#13a38c;
  --teal-dark:#0d7f6d;
  --ink:#1e1e1e;
  --muted:#6a6a6a;
  --grid:#d8d8d8;
  --stage:#dcdddf;
  --panel:#e6e7e8;
  --pale:#e3f1f8;
}
*{box-sizing:border-box;margin:0;padding:0}
html,body{width:1200px;height:963px;overflow:hidden}
body{background:var(--stage);font-family:"Montserrat",sans-serif;color:var(--ink);position:relative}
.slide{position:absolute;width:363px;height:204px;background:#fff;overflow:hidden;box-shadow:0 2px 5px rgba(0,0,0,.22)}
.a{position:absolute}
.brand{position:absolute;left:300px;top:8px;display:flex;align-items:center;gap:3px;color:var(--blue);font-weight:700;font-size:10px;line-height:1}
.brand i{width:7px;height:7px;border-radius:50%;background:var(--blue);display:block}
.pg{position:absolute;right:7px;bottom:6px;width:15px;height:15px;border:1.2px solid var(--teal);border-radius:50%;font-size:5px;font-weight:700;color:var(--teal);display:flex;align-items:center;justify-content:center}
.tx{font-size:4.2px;line-height:1.32;color:var(--muted);text-align:justify}
.tx+.tx{margin-top:4px}
.h-blue{color:var(--blue);font-weight:500}
.h-teal{color:var(--teal);font-weight:800}
.bul{display:flex;gap:6px;font-size:3.8px;line-height:1.35;color:var(--muted)}
.bul b{color:var(--blue);font-size:6px;line-height:1}
.photo{position:absolute}
.lg{display:flex;gap:3px;font-size:3.2px;color:var(--muted);line-height:1.3}
.lg i{width:5px;height:5px;border-radius:50%;background:var(--blue);flex:none;margin-top:1px}
.lg strong{display:block;color:var(--blue);font-size:5.6px;font-weight:600;margin-bottom:1px}
.lg.t i{background:var(--teal)}
.lg.t strong{color:var(--teal)}
.social{position:absolute;display:flex;gap:5px}
.social span{width:13px;height:13px;border-radius:3px;background:var(--blue);display:block}
.small-title{font-size:4.6px;color:#222;font-weight:700}
.rm-note{position:absolute;width:40px;font-size:3px;color:#777;line-height:1.3}
</style>
</head>
<body>

<!-- 01 Cover -->
<section class="slide" style="left:42px;top:49px;background:linear-gradient(135deg,#eef6fa,#dcecf5)">
  <div class="photo" role="img" aria-label="Soft blue DNA double helix illustration" style="left:130px;top:70px;width:233px;height:134px;background:radial-gradient(ellipse at 55% 45%,rgba(11,149,212,.35),rgba(11,149,212,0) 70%)"></div>
  <div class="a h-blue" style="left:18px;top:19px;font-size:10px;letter-spacing:.3px">PRESENTATION</div>
  <div class="a" style="left:18px;top:32px;font-size:25px;font-weight:800;color:var(--blue);line-height:1">BUSINESS</div>
  <div class="a" style="left:18px;top:62px;font-size:22px;font-weight:800;color:var(--teal);line-height:1">MARKETING</div>
  <div class="a" style="left:18px;top:95px;width:109px;height:1.2px;background:var(--teal)"></div>
  <div class="a" style="left:18px;top:106px;font-size:7px;letter-spacing:2.6px;color:var(--blue-deep)">www.halcyra.com</div>
  <div class="a" style="left:236px;top:24px;display:flex;align-items:center;gap:5px;color:var(--blue);font-weight:700;line-height:1">
    <i style="width:16px;height:16px;border-radius:50%;background:var(--blue);display:block"></i>
    <div><div style="font-size:20px">Halcyra</div><div style="font-size:8px;margin-top:2px">Therapeutics</div></div>
  </div>
  <div class="social" style="left:308px;top:174px"><span></span><span></span></div>
</section>

<!-- 02 Contents -->
<section class="slide" style="left:419px;top:49px">
  <div class="brand"><i></i>Halcyra</div>
  <div class="a" style="left:22px;top:29px;font-size:19px;font-weight:700;color:var(--blue)">Contents</div>
  <div class="a" style="left:22px;top:54px;width:314px;height:1.2px;background:var(--blue)"></div>
  <div class="a" style="left:22px;top:60px;width:320px;display:grid;grid-template-columns:170px 150px;row-gap:14px">
    <div style="display:flex;gap:6px"><b style="font-size:9px;color:var(--blue)">1.</b><div><div style="font-size:7.5px;font-weight:600;color:var(--teal)">Lorem ipsum</div><p class="tx" style="width:132px;margin-top:2px">Lorem ipsum dolor sit amet, consectetuer adipiscing elit, sed diam nonummy nibh euismod tincid</p></div></div>
    <div style="display:flex;gap:6px"><b style="font-size:9px;color:var(--blue)">4.</b><div><div style="font-size:7.5px;font-weight:600;color:var(--teal)">Lorem ipsum</div><p class="tx" style="width:132px;margin-top:2px">Lorem ipsum dolor sit amet, consectetuer adipiscing elit, sed diam nonummy nibh euismod tincid</p></div></div>
    <div style="display:flex;gap:6px"><b style="font-size:9px;color:var(--blue)">2.</b><div><div style="font-size:7.5px;font-weight:600;color:var(--teal)">Lorem ipsum</div><p class="tx" style="width:132px;margin-top:2px">Lorem ipsum dolor sit amet, consectetuer adipiscing elit, sed diam nonummy nibh euismod tincid</p></div></div>
    <div style="display:flex;gap:6px"><b style="font-size:9px;color:var(--blue)">5.</b><div><div style="font-size:7.5px;font-weight:600;color:var(--teal)">Lorem ipsum</div><p class="tx" style="width:132px;margin-top:2px">Lorem ipsum dolor sit amet, consectetuer adipiscing elit, sed diam nonummy nibh euismod tincid</p></div></div>
    <div style="display:flex;gap:6px"><b style="font-size:9px;color:var(--blue)">3.</b><div><div style="font-size:7.5px;font-weight:600;color:var(--teal)">Lorem ipsum</div><p class="tx" style="width:132px;margin-top:2px">Lorem ipsum dolor sit amet, consectetuer adipiscing elit, sed diam nonummy nibh euismod tincid</p></div></div>
    <div style="display:flex;gap:6px"><b style="font-size:9px;color:var(--blue)">6.</b><div><div style="font-size:7.5px;font-weight:600;color:var(--teal)">Lorem ipsum</div><p class="tx" style="width:132px;margin-top:2px">Lorem ipsum dolor sit amet, consectetuer adipiscing elit, sed diam nonummy nibh euismod tincid</p></div></div>
  </div>
  <div class="pg">02</div>
</section>

<!-- 03 Image + text -->
<section class="slide" style="left:795px;top:49px">
  <div class="photo" role="img" aria-label="DNA helix strand decoration" style="left:0;top:0;width:80px;height:30px;background:linear-gradient(90deg,rgba(11,149,212,.18),rgba(19,163,140,.18))"></div>
  <div class="photo" role="img" aria-label="DNA helix strand decoration" style="left:10px;top:174px;width:160px;height:30px;background:linear-gradient(90deg,rgba(19,163,140,.18),rgba(11,149,212,.18))"></div>
  <div class="brand"><i></i>Halcyra</div>
  <div class="photo" role="img" aria-label="Laboratory microscope photograph in blue tones" style="left:29px;top:36px;width:138px;height:132px;background:linear-gradient(135deg,#bfe0f2,#3f8fc6 55%,#d9eef8)"></div>
  <div class="a h-blue" style="left:174px;top:32px;font-size:9px">LOREM IPSUM DOLOR</div>
  <div class="a h-teal" style="left:174px;top:43px;font-size:8.5px">CONSECTETUER ADIPISCING ELIT</div>
  <div class="a" style="left:174px;top:58px;width:158px">
    <p class="tx">Lorem ipsum dolor sit amet, consectetuer adipiscing elit, sed diam nonummy nibh euismod tincidunt ut laoreet dolore magna aliquam erat volutpat. Ut wisi enim ad minim veniam, quis nostrud exerci tation ullam</p>
    <p class="tx">Lorem ipsum dolor sit amet, consectetuer adipiscing elit, sed diam nonummy nibh euismod tincidunt ut laoreet dolore magna aliquam erat volutpat. Ut wisi enim ad minim veniam, quis nostrud exerci tation ullam</p>
    <p class="tx">Lorem ipsum dolor sit amet, consectetuer adipiscing elit, sed diam nonummy nibh euismod tincidunt ut laoreet dolore magna aliquam erat volutpat. Ut wisi enim ad minim veniam, quis nostrud exerci</p>
    <p class="tx">Lorem ipsum dolor sit amet, consectetuer adipiscing elit, sed diam nonummy nibh euismod tincidunt ut laoreet dolore magna aliquam erat volutpat. Ut wisi enim ad minim veniam, quis nostrud exerci tation ullam</p>
  </div>
  <div class="pg">03</div>
</section>

<!-- 04 Two columns -->
<section class="slide" style="left:42px;top:270px">
  <div class="brand"><i></i>Halcyra</div>
  <div class="a" style="left:18px;top:17px;width:169px;height:169px;background:var(--panel)"></div>
  <div class="a" style="left:30px;top:25px;width:150px">
    <div class="h-blue" style="font-size:11px;line-height:1.15">LOREM IPSUM</div>
    <div class="h-teal" style="font-size:11px;line-height:1.15;margin-bottom:6px">DOLOR SIT AMET</div>
    <p class="tx">Lorem ipsum dolor sit amet, consectetuer adipiscing elit, sed diam nonummy nibh euismod tincidunt ut laoreet dolore magna aliquam erat volutpat. Ut wisi enim ad minim veniam, quis nostrud exerci tation ullamcorper suscipit lobortis nisl ut aliquip ex ea commodo consequat. Duis autem vel eum iriure dolor in hendrerit in vulputate velit esse</p>
    <p class="tx">Lorem ipsum dolor sit amet, consectetuer adipiscing elit, sed diam nonummy nibh euismod tincidunt ut laoreet dolore magna aliquam erat volutpat. Ut wisi enim ad minim veniam, quis nostrud exerci tation ullamcorper suscipit lobortis nisl ut aliquip ex ea commodo consequat. Duis autem vel eum iriure dolor in hendrerit in vulputate velit esse</p>
    <div class="bul" style="margin-top:9px"><b>▶</b><span>Lorem ipsum dolor sit amet, consectetuer adipiscing elit, sed diam nonummy nibh euismod tincidunt ut laoreet dolore magna</span></div>
    <div class="bul" style="margin-top:10px"><b>▷</b><span>Lorem ipsum dolor sit amet, consectetuer adipiscing elit, sed diam nonummy nibh euismod tincidunt ut laoreet dolore magna</span></div>
  </div>
  <div class="a" style="left:196px;top:25px;width:152px">
    <div class="h-blue" style="font-size:11px;line-height:1.15">LOREM IPSUM</div>
    <div class="h-teal" style="font-size:11px;line-height:1.15;margin-bottom:6px">DOLOR SIT AMET</div>
    <p class="tx">Lorem ipsum dolor sit amet, consectetuer adipiscing elit, sed diam nonummy nibh euismod tincidunt ut laoreet dolore magna aliquam erat volutpat. Ut wisi enim ad minim veniam, quis nostrud exerci tation ullamcorper suscipit lobortis nisl ut aliquip ex ea commodo consequat. Duis autem vel eum iriure dolor in hendrerit in vulputate velit esse</p>
    <p class="tx">Lorem ipsum dolor sit amet, consectetuer adipiscing elit, sed diam nonummy nibh euismod tincidunt ut laoreet dolore magna aliquam erat volutpat. Ut wisi enim ad minim veniam, quis nostrud exerci tation ullamcorper suscipit lobortis nisl ut aliquip ex ea commodo consequat. Duis autem vel eum iriure dolor in hendrerit in vulputate velit esse</p>
    <div class="bul" style="margin-top:9px"><b>▶</b><span>Lorem ipsum dolor sit amet, consectetuer adipiscing elit, sed diam nonummy nibh euismod tincidunt ut laoreet dolore magna</span></div>
    <div class="bul" style="margin-top:10px"><b>▷</b><span>Lorem ipsum dolor sit amet, consectetuer adipiscing elit, sed diam nonummy nibh euismod tincidunt ut laoreet dolore magna</span></div>
  </div>
  <div class="pg">04</div>
</section>

<!-- 05 Company overview -->
<section class="slide" style="left:419px;top:270px">
  <div class="brand"><i></i>Halcyra</div>
  <div class="a" style="left:22px;top:22px;line-height:1">
    <div style="font-size:12.5px;font-weight:700;color:var(--blue)">COMPANY</div>
    <div style="font-size:17px;font-weight:800;color:var(--teal);margin-top:2px">OVERVIEW</div>
  </div>
  <div class="a" style="left:22px;top:62px;width:146px">
    <p class="tx" style="text-align:left">Lorem ipsum dolor sit amet, consectetuer adipiscing elit, sed diam nonummy nibh euismod tincidunt ut laoreet dolore magna aliquam erat volutpat. Ut wisi enim ad minim veniam, quis nostrud exerci tation ullamcorper suscipit lobortis nisl ut aliquip ex ea commodo consequat. Duis autem vel eum iriure dolor in hendrerit i</p>
    <p class="tx" style="text-align:left">Lorem ipsum dolor sit amet, consectetuer adipiscing elit, sed diam nonummy nibh</p>
  </div>
  <svg class="a" style="left:184px;top:34px" width="160" height="82" viewBox="0 0 160 82" font-family="Montserrat,sans-serif">
    <g stroke="var(--grid)" stroke-width=".4">
      <line x1="10" y1="4" x2="156" y2="4"/><line x1="10" y1="15.5" x2="156" y2="15.5"/><line x1="10" y1="27" x2="156" y2="27"/><line x1="10" y1="38.5" x2="156" y2="38.5"/><line x1="10" y1="50" x2="156" y2="50"/><line x1="10" y1="61.5" x2="156" y2="61.5"/><line x1="10" y1="73" x2="156" y2="73"/>
    </g>
    <g font-size="4.5" fill="#444" text-anchor="end"><text x="7" y="6">60</text><text x="7" y="17">50</text><text x="7" y="29">40</text><text x="7" y="40">30</text><text x="7" y="52">20</text><text x="7" y="63">10</text><text x="7" y="75">0</text></g>
    <rect x="22" y="27" width="4" height="46" fill="var(--blue)"/><rect x="28" y="15.5" width="4" height="57.5" fill="var(--teal)"/>
    <rect x="54" y="61" width="4" height="12" fill="var(--blue)"/><rect x="60" y="33" width="4" height="40" fill="var(--teal)"/>
    <rect x="86" y="6" width="4" height="67" fill="var(--blue)"/><rect x="92" y="58" width="4" height="15" fill="var(--teal)"/>
    <rect x="118" y="13" width="4" height="60" fill="var(--teal)"/><rect x="124" y="38.5" width="4" height="34.5" fill="var(--blue)"/>
    <g font-size="5" fill="#333" text-anchor="middle"><text x="27" y="81">JAN</text><text x="59" y="81">FEB</text><text x="91" y="81">MAR</text><text x="123" y="81">APR</text></g>
  </svg>
  <svg class="a" style="left:18px;top:117px" width="158" height="72" viewBox="0 0 158 72" font-family="Montserrat,sans-serif">
    <g stroke="var(--grid)" stroke-width=".4">
      <line x1="10" y1="3" x2="156" y2="3"/><line x1="10" y1="12" x2="156" y2="12"/><line x1="10" y1="21" x2="156" y2="21"/><line x1="10" y1="30" x2="156" y2="30"/><line x1="10" y1="39" x2="156" y2="39"/><line x1="10" y1="48" x2="156" y2="48"/><line x1="10" y1="57" x2="156" y2="57"/>
    </g>
    <g font-size="3.8" fill="#444" text-anchor="end"><text x="7" y="4.5">60</text><text x="7" y="13.5">50</text><text x="7" y="22.5">40</text><text x="7" y="31.5">30</text><text x="7" y="40.5">20</text><text x="7" y="49.5">10</text><text x="7" y="58.5">0</text></g>
    <polyline points="14,57 29,48 44,31 59,17 74,45 89,26 104,40 119,32 134,26" fill="none" stroke="var(--blue)" stroke-width=".8"/>
    <polyline points="14,43 29,52 44,39 59,10 74,20 89,34 104,30 119,21 134,44" fill="none" stroke="var(--teal)" stroke-width=".8"/>
    <g font-size="2.6" fill="#555" text-anchor="middle"><text x="14" y="63">TEXT 01</text><text x="29" y="63">TEXT 02</text><text x="44" y="63">TEXT 03</text><text x="59" y="63">TEXT 04</text><text x="74" y="63">TEXT 05</text><text x="89" y="63">TEXT 06</text><text x="104" y="63">TEXT 07</text><text x="119" y="63">TEXT 08</text><text x="134" y="63">TEXT 09</text></g>
  </svg>
  <div class="a" style="left:184px;top:131px;display:grid;grid-template-columns:88px 70px;row-gap:10px">
    <div class="lg"><i></i><div><strong>Lorem ipsum</strong>Lorem ipsum dolor sit amet, consectetuer adipiscing elit, sed diam nonummy nibh euismod tincidunt</div></div>
    <div class="lg"><i></i><div><strong>Lorem ipsum</strong>Lorem ipsum dolor sit amet, consectetuer adipiscing elit, sed diam nonummy nibh euismod tincidunt</div></div>
    <div class="lg"><i></i><div><strong>Lorem ipsum</strong>Lorem ipsum dolor sit amet, consectetuer adipiscing elit, sed diam nonummy nibh euismod tincidunt</div></div>
    <div class="lg"><i></i><div><strong>Lorem ipsum</strong>Lorem ipsum dolor sit amet, consectetuer adipiscing elit, sed diam nonummy nibh euismod tincidunt</div></div>
  </div>
  <div class="pg">05</div>
</section>

<!-- 06 Market opportunities -->
<section class="slide" style="left:795px;top:270px">
  <div class="brand"><i></i>Halcyra</div>
  <div class="a" style="left:23px;top:18px;font-size:15.5px;font-weight:800;color:var(--blue);line-height:1.1">MARKET<br>OPPORTUNITIES</div>
  <div class="a" style="left:23px;top:58px;width:145px">
    <p class="tx" style="text-align:left">Lorem ipsum dolor sit amet, consectetuer adipiscing elit, sed diam nonummy nibh euismod tincidunt ut laoreet dolore magna aliquam erat volutpat. Ut wisi enim ad minim veniam, quis nostrud exerci tation ullamcorper suscipit lobortis nisl ut aliquip ex ea commodo consequat. Duis autem vel eum iriure dolor in hendrerit i</p>
    <p class="tx" style="text-align:left">Lorem ipsum dolor sit amet, consectetuer adipiscing elit, sed diam nonummy nibh</p>
  </div>
  <div class="a" style="left:195px;top:18px;font-size:5px;font-weight:600">CONSECTETUER ADIPISCING</div>
  <svg class="a" style="left:180px;top:28px" width="150" height="84" viewBox="0 0 150 84" font-family="Montserrat,sans-serif">
    <g stroke="var(--grid)" stroke-width=".4">
      <line x1="12" y1="3" x2="148" y2="3"/><line x1="12" y1="14" x2="148" y2="14"/><line x1="12" y1="25" x2="148" y2="25"/><line x1="12" y1="36" x2="148" y2="36"/><line x1="12" y1="47" x2="148" y2="47"/><line x1="12" y1="58" x2="148" y2="58"/><line x1="12" y1="69" x2="148" y2="69"/>
    </g>
    <g font-size="4.5" fill="#444" text-anchor="end"><text x="8" y="5">60</text><text x="8" y="16">50</text><text x="8" y="27">40</text><text x="8" y="38">30</text><text x="8" y="49">20</text><text x="8" y="60">10</text><text x="8" y="71">0</text></g>
    <rect x="20" y="25" width="16" height="44" fill="var(--blue)"/>
    <rect x="50" y="5" width="16" height="64" fill="var(--teal)"/>
    <rect x="80" y="53" width="16" height="16" fill="var(--blue)"/>
    <rect x="110" y="17" width="16" height="52" fill="var(--teal)"/>
    <g font-size="4.8" fill="#333" text-anchor="middle"><text x="28" y="79">JAN</text><text x="58" y="79">FEB</text><text x="88" y="79">MAR</text><text x="118" y="79">APR</text></g>
  </svg>
  <svg class="a" style="left:22px;top:120px" width="110" height="72" viewBox="0 0 110 72" font-family="Montserrat,sans-serif">
    <ellipse cx="55" cy="37" rx="50" ry="26" fill="var(--teal-dark)"/>
    <rect x="5" y="27" width="100" height="10" fill="var(--teal-dark)"/>
    <g transform="translate(55 27) scale(1 .52)">
      <circle r="41" fill="none" stroke="var(--blue)" stroke-width="18"/>
      <circle r="41" fill="none" stroke="var(--teal)" stroke-width="18" stroke-dasharray="103 154.6" transform="rotate(100)"/>
      <circle r="41" fill="none" stroke="var(--teal)" stroke-width="18" stroke-dasharray="51.5 206" transform="rotate(-20)"/>
    </g>
    <ellipse cx="55" cy="27" rx="24" ry="12" fill="#fff"/>
    <g font-size="7" font-weight="700" fill="#fff"><text x="12" y="30">40%</text><text x="48" y="10">20%</text><text x="82" y="24">20%</text><text x="52" y="46">20%</text></g>
  </svg>
  <div class="a" style="left:142px;top:130px;display:grid;grid-template-columns:106px 96px;row-gap:11px">
    <div class="lg"><i></i><div><strong>Lorem ipsum</strong>Lorem ipsum dolor sit amet, consectetuer adipiscing elit, sed diam nonummy nibh euismod tincidunt ut laoreet</div></div>
    <div class="lg t"><i></i><div><strong>Lorem ipsum</strong>Lorem ipsum dolor sit amet, consectetuer adipiscing elit, sed diam nonummy nibh euismod tincidunt ut laoreet</div></div>
    <div class="lg t"><i></i><div><strong>Lorem ipsum</strong>Lorem ipsum dolor sit amet, consectetuer adipiscing elit, sed diam nonummy nibh euismod tincidunt ut laoreet</div></div>
    <div class="lg"><i></i><div><strong>Lorem ipsum</strong>Lorem ipsum dolor sit amet, consectetuer adipiscing elit, sed diam nonummy nibh euismod tincidunt ut laoreet</div></div>
  </div>
  <div class="pg">06</div>
</section>

<!-- 07 Active intelligence -->
<section class="slide" style="left:42px;top:490px">
  <div class="brand"><i></i>Halcyra</div>
  <div class="a" style="left:18px;top:19px;line-height:1.15">
    <div class="h-blue" style="font-size:12px">ACTIVE</div>
    <div class="h-teal" style="font-size:12px">INTELLIGENCE</div>
  </div>
  <div class="a" style="left:18px;top:52px;width:148px">
    <p class="tx">Lorem ipsum dolor sit amet, consectetuer adipiscing elit, sed diam nonummy nibh euismod tincidunt ut laoreet dolore magna aliquam erat volutpat. Ut wisi enim ad minim veniam, quis nostrud exerci tation ullamcorper suscipit lobortis nisl ut aliquip ex ea commodo consequat. Duis autem vel eum iriure dolor in hendrerit in vulputate velit esse</p>
    <p class="tx">Lorem ipsum dolor sit amet, consectetuer adipiscing elit, sed diam nonummy nibh euismod tincidunt ut laoreet dolore magna aliquam erat volutpat. Ut wisi enim ad minim veniam, quis nostrud exerci tation ullamcorper suscipit lobortis nisl ut aliquip ex ea commodo consequat. Duis autem vel eum iriure dolor in hendrerit in vulputate velit esse</p>
    <div class="bul" style="margin-top:18px"><b>▶</b><span>Lorem ipsum dolor sit amet, consectetuer adipiscing elit, sed diam nonummy nibh euismod tincidunt ut laoreet dolore magna</span></div>
    <div class="bul" style="margin-top:10px"><b>▷</b><span>Lorem ipsum dolor sit amet, consectetuer adipiscing elit, sed diam nonummy nibh euismod tincidunt ut laoreet dolore magna</span></div>
  </div>
  <div class="a" style="left:256px;top:33px;width:107px;height:2px;background:var(--blue)"></div>
  <div class="a" style="left:173px;top:98px;width:2px;height:78px;background:var(--teal)"></div>
  <div class="a" style="left:173px;top:174px;width:85px;height:2px;background:var(--teal)"></div>
  <div class="photo" role="img" aria-label="Scientist working with a digital science interface photograph" style="left:179px;top:38px;width:184px;height:132px;background:linear-gradient(135deg,#2f7fb8,#9cc9e6 50%,#dfeef7)"></div>
  <div class="pg">07</div>
</section>

<!-- 08 Company costs -->
<section class="slide" style="left:419px;top:490px">
  <div class="brand"><i></i>Halcyra</div>
  <div class="a" style="left:0;top:20px;width:363px;text-align:center;font-size:17px;color:var(--blue);font-weight:500">COMPANY <b style="color:var(--teal);font-weight:800">COSTS</b></div>
  <div class="a" style="left:22px;top:45px;width:319px;text-align:center;font-size:3.9px;line-height:1.3;color:var(--muted)">
    <p>Lorem ipsum dolor sit amet, consectetuer adipiscing elit, sed diam nonummy nibh euismod tincidunt ut laoreet dolore magna aliquam erat volutpat. Ut wisi enim ad minim veniam, quis nostrud exerci tation ullamcorper suscipit lobortis nisl ut aliquip ex ea commodo consequat.</p>
    <p style="margin-top:4px">Duis autem vel eum iriure dolor in hendrerit in vulputate velit esse molestie consequat, vel illum dolore eu feugiat nulla facilisis at vero eros et accumsan et iusto odio dignissim qui blandit praesent luptatum zzril delenit augue duis dolore te feugait nulla facilisi.</p>
  </div>
  <svg class="a" style="left:0;top:80px" width="363" height="52" viewBox="0 0 363 52" font-family="Montserrat,sans-serif">
    <path d="M23 42 H326 L333 45 L326 48 H23Z" fill="var(--blue)"/>
    <path d="M148 42 H215 V48 H148Z" fill="var(--teal)"/><path d="M273 42 H326 L333 45 L326 48 H273Z" fill="var(--teal)"/>
    <g fill="none" stroke-width="5">
      <path d="M66 35 A20 20 0 1 1 102 35" stroke="var(--blue)"/>
      <path d="M129 35 A20 20 0 1 1 165 35" stroke="var(--teal)"/>
      <path d="M192 35 A20 20 0 1 1 228 35" stroke="var(--blue)"/>
      <path d="M256 35 A20 20 0 1 1 292 35" stroke="var(--teal)"/>
    </g>
    <circle cx="84" cy="24" r="8" fill="none" stroke="var(--blue)" stroke-width="1"/><path d="M84 19 V24 L87 26" stroke="var(--blue)" stroke-width="1" fill="none"/>
    <circle cx="147" cy="24" r="7" fill="var(--teal)"/><text x="147" y="26.5" font-size="7" fill="#fff" text-anchor="middle" font-weight="700">$</text>
    <g fill="none" stroke="var(--blue)" stroke-width="1"><ellipse cx="210" cy="20" rx="7" ry="2.5"/><path d="M203 20 V28 Q210 32 217 28 V20"/><path d="M203 24 Q210 28 217 24"/></g>
    <circle cx="273" cy="22" r="5" fill="none" stroke="var(--teal)" stroke-width="1.4"/><path d="M270 26 L265 31" stroke="var(--teal)" stroke-width="1.6"/>
    <g font-size="4.5" fill="#fff" font-weight="700"><text x="106" y="46.6">Step 01</text><text x="170" y="46.6">Step 02</text><text x="233" y="46.6">Step 03</text><text x="297" y="46.6">Step 04</text></g>
  </svg>
  <div class="a" style="left:84px;top:132px;width:1px;height:8px;background:#777"></div>
  <div class="a" style="left:147px;top:132px;width:1px;height:8px;background:#777"></div>
  <div class="a" style="left:210px;top:132px;width:1px;height:8px;background:#777"></div>
  <div class="a" style="left:274px;top:132px;width:1px;height:8px;background:#777"></div>
  <div class="a" style="left:52px;top:146px;width:256px;display:grid;grid-template-columns:repeat(4,64px);text-align:center">
    <div><div style="font-size:6.8px;font-weight:600;color:var(--teal)">Lorem Ipsum</div><p style="font-size:3px;color:#aaa;line-height:1.3;padding:1px 5px">Lorem ipsum dolor sit amet, consectetuer adipiscing elit, sed diam nonummy nibh euismod tincidunt ut laoreet dolore magna aliquam erat volutpat. Ut wisi</p></div>
    <div><div style="font-size:6.8px;font-weight:600;color:var(--teal)">Lorem Ipsum</div><p style="font-size:3px;color:#aaa;line-height:1.3;padding:1px 5px">Lorem ipsum dolor sit amet, consectetuer adipiscing elit, sed diam nonummy nibh euismod tincidunt ut laoreet dolore magna aliquam erat volutpat. Ut wisi</p></div>
    <div><div style="font-size:6.8px;font-weight:600;color:var(--teal)">Lorem Ipsum</div><p style="font-size:3px;color:#aaa;line-height:1.3;padding:1px 5px">Lorem ipsum dolor sit amet, consectetuer adipiscing elit, sed diam nonummy nibh euismod tincidunt ut laoreet dolore magna aliquam erat volutpat. Ut wisi</p></div>
    <div><div style="font-size:6.8px;font-weight:600;color:var(--teal)">Lorem Ipsum</div><p style="font-size:3px;color:#aaa;line-height:1.3;padding:1px 5px">Lorem ipsum dolor sit amet, consectetuer adipiscing elit, sed diam nonummy nibh euismod tincidunt ut laoreet dolore magna aliquam erat volutpat. Ut wisi</p></div>
  </div>
  <div class="pg">08</div>
</section>

<!-- 09 Text and list -->
<section class="slide" style="left:795px;top:490px">
  <div class="brand"><i></i>Halcyra</div>
  <div class="a" style="left:17px;top:35px;width:170px">
    <div class="h-blue" style="font-size:12px;line-height:1.15">LOREM IPSUM</div>
    <div class="h-teal" style="font-size:12px;line-height:1.15;margin-bottom:6px">DOLOR SIT AMET</div>
    <div style="font-size:4.6px;line-height:1.3;color:#333">
      <p style="margin-bottom:5px">▪ <b style="color:var(--blue)">Lorem ipsum</b> : dolor sit amet, consectetuer adipiscing elit, nonummy nibh euismod tincidunt ut laoreet dolore magna</p>
      <p style="margin-bottom:5px">▪ <b style="color:var(--blue)">Lorem ipsum</b> : dolor sit amet, consectetuer adipiscing elit, sed diam nonummy nibh euismod tincidunt ut laoreet dolore magna aliquam erat volutpat. Ut wisi enim ad min, quis nostrud exerci tation ullamcorper suscipit lobortis nisl</p>
      <p style="margin-bottom:5px">▪ <b style="color:var(--blue)">Lorem ipsum</b> : dolor sit amet, consectetuer adipis cing elit, sed diam nonummy nibh euismod tinci dunt ut laoreet magna aliquam erat volutpat.</p>
      <p style="margin-bottom:5px">▪ <b style="color:var(--blue)">Lorem ipsum</b> : dolor sit amet, consectetuer adipiscing nibh euismod tincidunt ut laoreet dolore magna</p>
      <p>▪ <b style="color:var(--blue)">Lorem ipsum</b> : dolor sit amet, consectetuer adipis cing elit, sed diam nonummy nibh euismod tinci dunt ut laoreet dolore.</p>
    </div>
  </div>
  <div class="a" style="left:204px;top:35px;width:150px">
    <div class="h-blue" style="font-size:11px;line-height:1.3">WHAT'S A DOMAIN?<br>IT'S THAT NAME UP</div>
    <div class="h-teal" style="font-size:11px;line-height:1.3;margin-bottom:6px">IN THE ADDRESS BAR.</div>
    <ul style="list-style:none;font-size:8px;line-height:1.95;color:#333">
      <li><span style="color:var(--blue)">▪</span> Fits your business or products</li>
      <li><span style="color:var(--blue)">▪</span> Is easy to spell and remember</li>
      <li><span style="color:var(--blue)">▪</span> Fits your business or products</li>
      <li><span style="color:var(--blue)">▪</span> Is easy to spell and remember</li>
      <li><span style="color:var(--blue)">▪</span> Fits your business or products</li>
      <li><span style="color:var(--blue)">▪</span> Is easy to spell and remember</li>
    </ul>
  </div>
  <div class="pg">09</div>
</section>

<!-- 10 Roadmap -->
<section class="slide" style="left:42px;top:710px">
  <div class="brand"><i></i>Halcyra</div>
  <svg class="a" style="left:0;top:0" width="363" height="204" viewBox="0 0 363 204" font-family="Montserrat,sans-serif">
    <path d="M307 150 V124" stroke="var(--teal)" stroke-width="1.2" stroke-dasharray="1.5 2" fill="none"/>
    <circle cx="307" cy="155" r="2.5" fill="var(--teal)"/>
    <path d="M307 155 C260 160 210 155 190 140 C175 128 190 115 230 110 C265 105 290 95 285 80" stroke="var(--blue)" stroke-width="1.4" fill="none"/>
    <path d="M186 85 V114" stroke="var(--teal)" stroke-width="1.2" stroke-dasharray="1.5 2" fill="none"/>
    <path d="M241 62 V80" stroke="var(--teal)" stroke-width="1.2" stroke-dasharray="1.5 2" fill="none"/>
    <path d="M142 57 C150 70 160 60 176 66 C200 72 230 70 241 78" stroke="var(--blue)" stroke-width="1.2" fill="none"/>
    <path d="M118 38 C118 45 130 40 142 45" stroke="var(--blue)" stroke-width="1" fill="none"/>
    <path d="M168 41 V48" stroke="var(--teal)" stroke-width="1" stroke-dasharray="1 1.5"/>
    <path d="M307 122 L300 113 A24 24 0 1 1 314 113Z" fill="var(--teal)"/>
    <circle cx="307" cy="92" r="20" fill="#fff"/>
    <text x="307" y="103" font-size="30" font-weight="700" fill="var(--blue)" text-anchor="middle">1</text>
    <circle cx="186" cy="73" r="13" fill="var(--teal)"/><circle cx="186" cy="73" r="10" fill="#fff"/><text x="186" y="78.5" font-size="15" font-weight="700" fill="var(--blue)" text-anchor="middle">2</text>
    <circle cx="241" cy="49" r="11" fill="var(--teal)"/><circle cx="241" cy="49" r="8.5" fill="#fff"/><text x="241" y="54" font-size="13" font-weight="700" fill="var(--blue)" text-anchor="middle">3</text>
    <circle cx="142" cy="49" r="7.5" fill="var(--teal)"/><circle cx="142" cy="49" r="5.8" fill="#fff"/><text x="142" y="52.5" font-size="9" font-weight="700" fill="var(--blue)" text-anchor="middle">4</text>
    <circle cx="168" cy="36" r="5.5" fill="var(--teal)"/><circle cx="168" cy="36" r="4.2" fill="#fff"/><text x="168" y="38.5" font-size="6.5" font-weight="700" fill="var(--blue)" text-anchor="middle">5</text>
    <circle cx="118" cy="35" r="4.2" fill="var(--teal)"/><circle cx="118" cy="35" r="3.2" fill="#fff"/><text x="118" y="36.8" font-size="5" font-weight="700" fill="var(--blue)" text-anchor="middle">6</text>
  </svg>
  <div class="rm-note" style="left:70px;top:32px"><b class="small-title">LOREM IPSUM</b><br>Lorem ipsum dolor sit amet, consectetuer adipiscing elit, sed diam nonummy nibh euismod tincid</div>
  <div class="rm-note" style="left:180px;top:27px"><b class="small-title">LOREM IPSUM</b><br>Lorem ipsum dolor sit amet, consectetuer adipiscing elit, sed diam nonummy nibh euismod tincid</div>
  <div class="rm-note" style="left:258px;top:30px"><b class="small-title">LOREM IPSUM</b><br>Lorem ipsum dolor sit amet, consectetuer adipiscing elit, sed diam nonummy nibh euismod tincid</div>
  <div class="rm-note" style="left:130px;top:79px"><b class="small-title">LOREM IPSUM</b><br>Lorem ipsum dolor sit amet, consectetuer adipiscing elit, sed diam nonummy nibh euismod tincid</div>
  <div class="rm-note" style="left:245px;top:104px"><b class="small-title">LOREM IPSUM</b><br>Lorem ipsum dolor sit amet, consectetuer adipiscing elit, sed diam nonummy nibh euismod tincid</div>
  <div class="a" style="left:27px;top:100px;line-height:1.05">
    <div style="font-size:10px;color:var(--teal);letter-spacing:.5px">TIMELINE OF</div>
    <div style="font-size:17px;color:var(--teal);font-weight:500">ROADMAP</div>
    <div style="font-size:8px;color:var(--blue);font-weight:700;margin-top:1px">FOR 2 YEARS</div>
  </div>
  <div class="a" style="left:27px;top:153px;display:flex;gap:28px">
    <div style="display:flex;gap:4px"><span style="width:21px;height:21px;border-radius:50%;background:var(--blue);color:#fff;font-weight:800;font-size:11px;display:flex;align-items:center;justify-content:center">A</span><div style="font-size:3px;color:#777;line-height:1.3;width:40px"><b style="font-size:9px;color:#222;display:block;line-height:1.1">2019</b>Lorem ipsum dolor sit amet, consectetuer adipiscing elit, sed diam</div></div>
    <div style="display:flex;gap:4px"><span style="width:21px;height:21px;border-radius:50%;background:var(--blue);color:#fff;font-weight:800;font-size:11px;display:flex;align-items:center;justify-content:center">B</span><div style="font-size:3px;color:#777;line-height:1.3;width:40px"><b style="font-size:9px;color:#222;display:block;line-height:1.1">2020</b>Lorem ipsum dolor sit amet, consectetuer adipiscing elit, sed diam</div></div>
  </div>
  <div class="pg">10</div>
</section>

<!-- 11 Team -->
<section class="slide" style="left:419px;top:710px">
  <div class="brand"><i></i>Halcyra</div>
  <div class="a" style="left:0;top:31px;width:363px;text-align:center;font-size:11.5px;color:var(--teal);font-weight:700">TEAM MEMBERS AND ADVISORS</div>
  <div class="a" style="left:22px;top:51px;width:319px;text-align:center;font-size:3.9px;line-height:1.3;color:var(--muted)">
    <p>Lorem ipsum dolor sit amet, consectetuer adipiscing elit, sed diam nonummy nibh euismod tincidunt ut laoreet dolore magna aliquam erat volutpat. Ut wisi enim ad minim veniam, quis nostrud exerci tation ullamcorper suscipit lobortis nisl ut aliquip ex ea commodo consequat. Duis autem</p>
    <p style="margin-top:4px">Lorem ipsum dolor sit amet, cons ectetuer adipiscing elit, sed diam nonummy nibh euismod tincidunt ut laoreet dolore magna aliquam erat volutpat.</p>
  </div>
  <div class="a" style="left:0;top:88px;width:363px;height:85px;background:var(--teal)"></div>
  <div class="a" style="left:12px;top:93px;width:340px;display:grid;grid-template-columns:repeat(4,85px);text-align:center;color:#fff">
    <div><div role="img" aria-label="Team member portrait" style="width:31px;height:31px;margin:0 auto;border-radius:50%;border:1.5px solid #fff;background:linear-gradient(#e8f1f8,#9cc6e3)"></div><div style="font-size:6px;font-weight:600;margin-top:3px">OWEN HALE</div><p style="font-size:2.6px;line-height:1.35;padding:2px 13px">Ipsum dolor sit amet, cons ectetuer adipiscing elit, sed diam nonummy nibh euismod tincidunt ut laoreet dolore magna aliquam erat volutpat. Ut wisi enim ad minim veniam, quis nostrud</p></div>
    <div><div role="img" aria-label="Team member portrait" style="width:31px;height:31px;margin:0 auto;border-radius:50%;border:1.5px solid #fff;background:linear-gradient(#e8f1f8,#9cc6e3)"></div><div style="font-size:6px;font-weight:600;margin-top:3px">NADIA REYES</div><p style="font-size:2.6px;line-height:1.35;padding:2px 13px">Ipsum dolor sit amet, cons ectetuer adipiscing elit, sed diam nonummy nibh euismod tincidunt ut laoreet dolore magna aliquam erat volutpat. Ut wisi enim ad minim veniam, quis nostrud</p></div>
    <div><div role="img" aria-label="Team member portrait" style="width:31px;height:31px;margin:0 auto;border-radius:50%;border:1.5px solid #fff;background:linear-gradient(#e8f1f8,#9cc6e3)"></div><div style="font-size:6px;font-weight:600;margin-top:3px">OWEN HALE</div><p style="font-size:2.6px;line-height:1.35;padding:2px 13px">Ipsum dolor sit amet, cons ectetuer adipiscing elit, sed diam nonummy nibh euismod tincidunt ut laoreet dolore magna aliquam erat volutpat. Ut wisi enim ad minim veniam, quis nostrud</p></div>
    <div><div role="img" aria-label="Team member portrait" style="width:31px;height:31px;margin:0 auto;border-radius:50%;border:1.5px solid #fff;background:linear-gradient(#e8f1f8,#9cc6e3)"></div><div style="font-size:6px;font-weight:600;margin-top:3px">NADIA REYES</div><p style="font-size:2.6px;line-height:1.35;padding:2px 13px">Ipsum dolor sit amet, cons ectetuer adipiscing elit, sed diam nonummy nibh euismod tincidunt ut laoreet dolore magna aliquam erat volutpat. Ut wisi enim ad minim veniam, quis nostrud</p></div>
  </div>
  <div class="pg">11</div>
</section>

<!-- 12 Thank you -->
<section class="slide" style="left:795px;top:710px">
  <div class="photo" role="img" aria-label="Glowing blue DNA strands photograph with a teal helix strand along its edge" style="left:0;top:0;width:363px;height:204px;clip-path:polygon(118px 0,363px 0,363px 204px,175px 204px);background:linear-gradient(100deg,#13a38c 0,#0b95d4 18%,#0a4a96 55%,#062a5e)"></div>
  <div class="a" style="left:18px;top:28px;display:flex;align-items:center;gap:5px;color:var(--blue);font-weight:700;line-height:1">
    <i style="width:16px;height:16px;border-radius:50%;background:var(--blue);display:block"></i>
    <div><div style="font-size:22px">Halcyra</div><div style="font-size:8.5px;margin-top:2px">Therapeutics</div></div>
  </div>
  <div class="a" style="left:16px;top:118px;font-size:17px;font-weight:800;color:#111">THANK YOU</div>
  <div class="a" style="left:16px;top:147px;font-size:9px;font-weight:800;color:var(--teal)">CONTACT US</div>
  <div class="a" style="left:16px;top:161px;font-size:5.8px;line-height:1.5;color:#222">
    <div><span style="color:var(--teal)">●</span> 555-010-4477</div>
    <div><span style="color:var(--teal)">●</span> hello@brightlane.co</div>
    <div><span style="color:var(--teal)">●</span> Your address, your city, box 88900</div>
  </div>
  <div class="social" style="left:318px;top:176px"><span style="background:#fff;opacity:.9"></span><span style="background:#fff;opacity:.9"></span></div>
</section>

</body>
</html>
```